Hurricane Damage Public Adjuster Billboard

I have created several projects with you and have several great designs. I need to format them into a Billboard for upcoming Hurricane Season. Need done in a month. Im also in process of getting an eye catching and easy to remember 800# Vanity phone number like Call 800-Stormsafe or 800- Need Help? My included past Pixel Bazaar projects will give you an idea of what colors, schemes, and designs I gravitate towards. 3 past Design projects were 1) 2 Logos where I picked the 1st place and the 2nd place and 2) Index Card where I picked the winner as the Index Card and the 2nd place as a Post Card. Point is, I will pick and pay for 2 winners if they're good. This should help to sweeten the pot. Also, please look at my website for ideas that I like:

www.CedarlineClaimHelp.com
I want people to feel that I am the best and highest. Level.

I've been getting a lot of quick half effort designs basically cut & pasting my previous projects. Please don't rush and take your time to be creative. A an example, my Biggest Competitor is Tamarack Public Adjusting. Their colors are Black and Gold while mine are Blue, White, and Black with a highlight of Orange if possible. I JUST imported a picture of their BillBoard. I need mine better and BLOW AWAY THEIRS. Terms like "Don't be Victimized Twice ?, Don't let the Hurricane Ruin your Life?". "Get Fairly Paid & Move On" "Our Clients Claims are VIP?
Updates

I'm getting a lot of quick half effort ones. I'd rather you take your time and really put some thoughts and effort into it. My Biggest Competitor is Tamarack Public Adjusting. They have black & gold colors, while I have Blue, Black, and white.

It needs to blow theirs away. I have imported their Billboard for comparative purposes.

Guy's,
I'll make it easier for you in what I'm looking for. Please look at the Tamarack Billboard picture attached.

1) Put my "Blue Shield" to the left, replacing their logo
2) change color patterns from their (Black, Gold, White) to my color schemes of (Black, Blue, White)
3) I want to see my name where their is:

THE
Cedarline Claim Help
EXPERT & LOCAL Public Adjusters
"FOR THE POLICYHOLDER!!"

4) to the right, add the A+Rated logo and QRT+ Accredited logo, 5 Star Zorvex Rated logo, 5 Start PORCHLINK Highly Rated logo, etc..

5) the right side is where you can be creative as I will not have a picture of me there.

"20+ Years of Experience, Recovering Millions for our VIP Clients"

"Your Best, Locally-Based Private Adjuster & Advocate'
"FOR THE POLICYHOLDER!!"

"Don't be victimized Twice!!"

"Don't let the Hurricane Ruin Your Life!!"

This should really help. Also, refer to my website, maybe a couple testimonial fillers?

Thanks all,

marcus@CedarlineClaimHelp.com

Just imported a few awards that would look great to the right side with all the other 5 Star Ratings and accolades.
This right section could be titled like zmy Website:

5 Star Reviews, Ratings & Awards:
4-5 Logos underneath?

Target Market(s)

Coastal place where a Hurricane 🌀 🌀 Hits

Industry/Entity Type

Hurricane Public Insurance Adjuster

Font styles to use
Sans Serif
Other font styles liked:
• Zurich fonts

Colors
0054AA
0677BA
7BADD7
CADEEF
E8F1F8
EE7325
F08F49
F5BC92
FAE3D3
FDF4ED

Requirements
Must have
• Use my past project logos, colors, and schemes to create eye grabbing BillBoard
Nice to have
Should not have
• Not be too busy, must be Easy to Read, Eye Catchy

```html
<!DOCTYPE html>
<html lang="en">
<head>
<meta charset="utf-8">
<title>Cedarline Claim Help – Hurricane Season Billboard</title>
<link href="https://fonts.googleapis.com/css2?family=Anton&family=Oswald:wght@500;600;700&family=Montserrat:ital,wght@0,500;0,600;0,700;1,500&display=swap" rel="stylesheet">
<style>
  :root {
    --ink: #141414;
    --blue-bright: #1aa9ea;
    --blue-mid: #0f8fd6;
    --blue-deep: #0677BA;
    --brand-blue: #17a4e4;
    --white: #ffffff;
    --rating-red: #e0202a;
    --badge-blue: #1d5a8e;
    --star-gold: #f3b400;
    --porch-green: #5ac13a;
    --page: #e8eef3;
  }
  * { margin: 0; padding: 0; box-sizing: border-box; }
  html, body { width: 1200px; height: 971px; overflow: hidden; background: var(--page); }
  .billboard {
    position: absolute; left: 40px; top: 244px;
    width: 1120px; height: 482px;
    background: var(--ink); overflow: hidden;
    box-shadow: 0 10px 30px rgba(0,0,0,.25);
  }
  .billboard-shapes { position: absolute; inset: 0; }
  .abs { position: absolute; }
  .brand-mark {
    left: 258px; top: 40px; width: 124px; height: 124px; border-radius: 50%;
    background: linear-gradient(160deg, var(--blue-deep), var(--blue-bright));
  }
  .brand-name {
    left: 60px; width: 520px; text-align: center; white-space: nowrap;
    font-family: "Montserrat", sans-serif; font-weight: 500; color: var(--brand-blue);
  }
  .brand-name--main { top: 196px; font-size: 44px; letter-spacing: 1px; }
  .brand-name--sub { top: 253px; font-size: 28px; letter-spacing: 3px; }
  .rule { top: 269px; height: 2px; width: 100px; background: var(--brand-blue); }
  .rule--left { left: 100px; }
  .rule--right { left: 440px; }
  .brand-line {
    left: 60px; top: 302px; width: 520px; text-align: center; white-space: nowrap;
    font-family: "Montserrat", sans-serif; font-weight: 500; font-size: 20px;
    letter-spacing: 2.4px; color: var(--white);
  }
  .brand-tag {
    left: 60px; top: 340px; width: 520px; text-align: center; white-space: nowrap;
    font-family: "Montserrat", sans-serif; font-style: italic; font-weight: 500;
    font-size: 25px; color: var(--brand-blue);
  }
  .call-label {
    left: 26px; top: 412px; font-family: "Anton", sans-serif; font-size: 23px;
    line-height: 28px; color: var(--white); letter-spacing: .5px;
  }
  .phone-icon { left: 140px; top: 408px; width: 44px; height: 44px; }
  .phone-number {
    left: 192px; top: 402px; font-family: "Montserrat", sans-serif; font-weight: 700;
    font-size: 42px; color: var(--white); letter-spacing: .5px; white-space: nowrap;
  }
  .website {
    left: 152px; top: 455px; font-family: "Oswald", sans-serif; font-weight: 600;
    font-size: 18px; color: var(--white); letter-spacing: 1.6px; white-space: nowrap;
  }
  .headline {
    left: 636px; width: 480px; top: 30px; text-align: center; white-space: nowrap;
    font-family: "Anton", sans-serif; font-weight: 400; font-size: 44px; line-height: 56px;
    color: var(--white); text-shadow: 0 2px 3px rgba(0,0,0,.25);
  }
  .subline {
    left: 650px; width: 460px; top: 162px; text-align: center; white-space: nowrap;
    font-family: "Oswald", sans-serif; font-weight: 700; font-style: italic;
    font-size: 16px; color: var(--white);
  }
  .experience {
    left: 680px; width: 420px; top: 214px; text-align: center;
    font-family: "Oswald", sans-serif; font-weight: 600; font-size: 19px;
    line-height: 25px; color: var(--white);
  }
  .awards-title {
    left: 700px; width: 400px; top: 290px; text-align: center; white-space: nowrap;
    font-family: "Oswald", sans-serif; font-weight: 600; font-size: 20px;
    color: var(--white); letter-spacing: .3px;
  }
  .award-rating {
    left: 690px; top: 424px; font-family: "Montserrat", sans-serif; white-space: nowrap;
    font-weight: 600; font-size: 22px; color: var(--rating-red);
  }
  .award-badge {
    left: 815px; top: 412px; width: 84px; height: 36px; border-radius: 4px;
    background: var(--badge-blue);
  }
  .award-badge-caption {
    left: 815px; top: 451px; width: 84px; text-align: center; white-space: nowrap;
    font-family: "Montserrat", sans-serif; font-weight: 600; font-size: 8px; color: var(--badge-blue);
  }
  .award-review {
    left: 908px; top: 406px; width: 96px; text-align: center;
    font-family: "Montserrat", sans-serif; font-weight: 600; font-size: 24px; color: var(--blue-deep);
  }
  .stars {
    left: 921px; top: 440px; font-size: 14px; letter-spacing: 1px; color: var(--star-gold);
    font-family: sans-serif;
  }
  .award-porch {
    left: 1010px; top: 422px; font-family: "Montserrat", sans-serif; white-space: nowrap;
    font-weight: 700; font-size: 16px; color: var(--porch-green);
  }
</style>
</head>
<body>
<main class="billboard">
  <svg class="billboard-shapes" width="1120" height="482" viewBox="0 0 1120 482" aria-hidden="true">
    <defs>
      <linearGradient id="panelBlue" x1="0" y1="0" x2="1" y2="1">
        <stop offset="0" stop-color="#1aa9ea"/>
        <stop offset="1" stop-color="#0b82c9"/>
      </linearGradient>
      <linearGradient id="bandBlue" x1="0" y1="0" x2="1" y2="0">
        <stop offset="0" stop-color="#0f8fd6"/>
        <stop offset="1" stop-color="#1aa9ea"/>
      </linearGradient>
    </defs>
    <path d="M632 0 H1120 V400 H720 C668 320 632 190 632 0 Z" fill="url(#panelBlue)"/>
    <path d="M0 388 H540 C585 388 605 400 625 425 L672 482 H0 Z" fill="url(#bandBlue)"/>
    <path d="M652 400 H1120 V482 H722 Z" fill="#ffffff"/>
  </svg>

  <div class="abs brand-mark" role="img" aria-label="Brand shield mark"></div>
  <div class="abs brand-name brand-name--main">CEDARLINE</div>
  <div class="abs rule rule--left"></div>
  <div class="abs brand-name brand-name--sub">CLAIM HELP</div>
  <div class="abs rule rule--right"></div>
  <div class="abs brand-line">EXPERT &amp; LOCAL PUBLIC ADJUSTERS</div>
  <div class="abs brand-tag">"FOR THE POLICYHOLDER!!"</div>

  <div class="abs call-label">CALL US<br>TODAY!</div>
  <svg class="abs phone-icon" viewBox="0 0 44 44" aria-hidden="true">
    <circle cx="22" cy="22" r="19" fill="none" stroke="#fff" stroke-width="3.5"/>
    <path d="M15 12 l5 -1 l3 6 l-3 3 c2 4 4 6 7 7 l3 -3 l6 3 l-1 5 c-1 2 -4 2 -7 1 c-6 -3 -11 -8 -13 -14 c-1 -3 -1 -6 0 -7 z" fill="#fff"/>
  </svg>
  <div class="abs phone-number">(555) 318-4420</div>
  <div class="abs website">WWW.CEDARLINECLAIMHELP.COM</div>

  <h1 class="abs headline">DON'T LET THE HURRICANE<br>RUIN YOUR LIFE!!</h1>
  <p class="abs subline">YOUR BEST, LOCALLY-BASED PRIVATE ADJUSTER &amp; ADVOCATE!</p>
  <p class="abs experience">20+ YEARS OF EXPERIENCE, RECOVERING<br>MILLIONS FOR OUR VIP CLIENTS!</p>
  <p class="abs awards-title">5 STAR REVIEWS, RATINGS &amp; AWARDS:</p>

  <div class="abs award-rating">A+ Rating</div>
  <div class="abs award-badge"></div>
  <div class="abs award-badge-caption">QRT+ Rating: A+</div>
  <div class="abs award-review">Zorvex</div>
  <div class="abs stars">★★★★★</div>
  <div class="abs award-porch">PORCHLINK</div>
</main>
</body>
</html>
```